Boutique Shoe Bag Race wear Business Card Design

We are a new luxury shoe bag, jewellery and race wear store stocking local and international designers. Located in the fashion precinct of beautiful Calloway Cove famous in Sydney Australia. Stocking French jewellery and shoes such as Renaud valmiers plus Australian made. Looking at quality and service and looking after the locals and tourists.
Ideas: White background, Black writing in bold engravers, logo in middle of Marlow and Boutique a gold horseshoe (facing upright so the curve is at the bottom) with a black stiletto inside. French clover silver and black border (not irish clover the French lattice type look)
Updates

Marlow Atelier

I open 8/4 so require business card design ASAP.

Please place gold horseshoe facing upwards with the black stiletto inside.

Bold engravers writing for business name.

I will have my phone number tomorrow to update.

Border in similar/same style as attached picture with black/silver clover French design.

Thank you. Tessa                                   

Industry/Entity Type

Fashion

Contact Information for Business Card

Marlow Atelier
Boutique Owner Tessa Wrenfield
41B Parrin Lane
Calloway Cove NSW 2093 Australia
0471239046
02 **** *TBA
info@marlowatelier.com.au
Fanpage.com/MarlowAtelier
www.marlowatelier.com.au

Font styles to use
Other font styles liked:
• Bold Engravers

Requirements
Must have
• Info on one side including business name and logo with black stiletto and gold horse shoe. reverse side with French clover border and Larger name Marlow Atelier with logo in centre.
Should not have
• irish clover
French script
horseshoe upside down

```html
<!DOCTYPE html>
<html lang="en">
<head>
<meta charset="utf-8">
<title>Marlow Atelier — Business Card</title>
<link rel="stylesheet" href="https://fonts.googleapis.com/css2?family=Cinzel:wght@700&family=Questrial&display=swap">
<style>
  :root {
    --backdrop: #ebebeb;
    --lattice-dark: #1f1d1e;
    --lattice-mid: #3a3839;
    --card-white: #ffffff;
    --ink: #231f20;
    --ink-soft: #2b2b2b;
    --icon-grey: #8a8a8a;
    --gold: #c39a45;
  }
  * { margin: 0; padding: 0; box-sizing: border-box; }
  html, body { width: 1200px; height: 1000px; overflow: hidden; }
  body { background: var(--backdrop); position: relative; font-family: "Questrial", "Century Gothic", sans-serif; color: var(--ink); }

  .card { position: absolute; }
  .card-border {
    position: absolute; inset: 0;
    background: radial-gradient(ellipse at 50% 40%, var(--lattice-mid), var(--lattice-dark) 75%);
  }
  .card-face { position: absolute; background: var(--card-white); }

  .card--front { left: 181px; top: 19px; width: 858px; height: 466px; }
  .card--front .card-face { left: 47px; top: 47px; width: 765px; height: 371px; }

  .card--back { left: 181px; top: 510px; width: 855px; height: 464px; }
  .card--back .card-face { left: 47px; top: 46px; width: 762px; height: 372px; }

  .brand-name {
    font-family: "Cinzel", "Times New Roman", serif; font-weight: 700;
    color: var(--ink); white-space: nowrap;
  }
  .brand-mark { display: inline-block; border-radius: 50%; background: var(--gold); }

  .front-lockup {
    position: absolute; left: 0; right: 0; top: 118px;
    display: flex; align-items: center; justify-content: center; gap: 16px;
  }
  .front-lockup .brand-name { font-size: 46px; letter-spacing: 5px; }
  .front-lockup .brand-mark { width: 92px; height: 92px; }
  .front-url {
    position: absolute; left: 0; right: 0; top: 305px;
    text-align: center; font-size: 27px; color: var(--ink-soft);
  }

  .back-name { position: absolute; left: 16px; top: 34px; font-size: 37px; letter-spacing: 3.5px; }
  .back-mark { position: absolute; left: 640px; top: 26px; width: 90px; height: 90px; }
  .person-name { position: absolute; left: 16px; top: 126px; font-size: 29px; font-weight: 700; -webkit-text-stroke: 0.6px var(--ink); }
  .person-role { position: absolute; left: 16px; top: 172px; font-size: 29px; }

  .contact-list { position: absolute; left: 13px; top: 238px; list-style: none; font-size: 24px; line-height: 32px; }
  .contact-list li { display: flex; align-items: center; gap: 4px; white-space: nowrap; }
  .contact-icon { width: 21px; height: 21px; flex: none; }
  .social-square { width: 18px; height: 18px; margin: 0 2px 0 1px; background: var(--icon-grey); flex: none; }

  .address { position: absolute; right: 27px; top: 266px; text-align: right; font-size: 24px; line-height: 32px; font-style: normal; }
</style>
</head>
<body>

<section class="card card--front" aria-label="Business card front">
  <div class="card-border" role="img" aria-label="Black and silver French lattice clover pattern border"></div>
  <div class="card-face">
    <div class="front-lockup">
      <span class="brand-name">MARLOW</span>
      <span class="brand-mark" aria-hidden="true"></span>
      <span class="brand-name">ATELIER</span>
    </div>
    <p class="front-url">www.marlowatelier.com.au</p>
  </div>
</section>

<section class="card card--back" aria-label="Business card back">
  <div class="card-border" role="img" aria-label="Black and silver French lattice clover pattern border"></div>
  <div class="card-face">
    <p class="brand-name back-name">MARLOW ATELIER</p>
    <span class="brand-mark back-mark" aria-hidden="true"></span>

    <p class="person-name">Tessa Wrenfield</p>
    <p class="person-role">Boutique Owner</p>

    <ul class="contact-list">
      <li>
        <svg class="contact-icon" viewBox="0 0 21 21" aria-hidden="true">
          <rect x="6" y="1.5" width="9" height="18" rx="1.5" fill="none" stroke="var(--icon-grey)" stroke-width="1.6"/>
          <line x1="6" y1="15.5" x2="15" y2="15.5" stroke="var(--icon-grey)" stroke-width="1.2"/>
        </svg>
        0471239046 / 02 9184 6620
      </li>
      <li>
        <svg class="contact-icon" viewBox="0 0 21 21" aria-hidden="true">
          <rect x="1.5" y="5" width="18" height="12" fill="none" stroke="var(--icon-grey)" stroke-width="1.4"/>
          <polyline points="1.5,5 10.5,12 19.5,5" fill="none" stroke="var(--icon-grey)" stroke-width="1.4"/>
        </svg>
        info@marlowatelier.com.au
      </li>
      <li><span class="social-square" aria-hidden="true"></span>Fanpage.com/MarlowAtelier</li>
      <li><span class="social-square" aria-hidden="true"></span>snapview.com/marlowatelier</li>
    </ul>

    <address class="address">
      41B Parrin Lane<br>
      Calloway Cove<br>
      NSW 2093 Australia
    </address>
  </div>
</section>

</body>
</html>
```